Australia-Wide Industry Leader Bookkeeping Business Website Design Required

We need a website designed for our 10 year old bookkeeping business, Barwick & Lund. Barwick & Lund has been servicing the local & interstate communities of Australia, providing first-class BAS & Bookkeeping services with a personal touch unmatched by anyone else in the county.

What began 10 years ago as a small business focusing on family, friends and the local community, it has since grown into a well respected business with 95% of their business based solely on word of mouth and personal referrals from around Australia.

We would like to see designs that incorporate our existing brand/logo. The colours to be used on the website should be colours that work well with our logo. The design should communicate maturity, trust and confidence with a Web 2.0 look and feel.

We have produced mockups of the entire website as well as assets used in the mockups. Please reference the attached files. The mockups are an example of all the design elements that we want on each page. Designers are encouraged to use the mockups as a guideline only and for designers to use their own creativity.
Updates

This message is for new graphic designers who are considering commencing work on this project. Thank you for expressing an interest in our project. We would like to inform you that this project is close to completion as we have a number designs under very serious consideration.

We are currently in a position where we are disinterested providing feedback to improve on new designs submitted. We will provide feedback to improve new designs only if the submitted designs are very close to what we want for our website, and will only require 1 or 2 revision rounds to refine before the project completion date we will not work with designers to refine their newly submitted designs.

We feel that it is important for all designers to know the above information as we feel that your time and effort may be better spent working on another project.

Thank you for your understanding.

A big thank you for all the designs submitted. We are now in the process of selecting a design. Please be patient during this process. Thank you.

Target Market(s)

Busy Business Owners

Industry/Entity Type

Small Business

Requirements
Must have
• We require a rectangular "slide show" type feature to serve as a "teaser" to arouse the emotions of our website visitors. Each slide asks a specific question. The questions are:

- Is your paperwork in a mess?
- Do you need to get organised for the end of financial year?
- Are you sick & tired of endless amounts of paperwork & BASs?
- Do you feel frustrated & annoyed because you know your books need to be done?
- Do you lack the time & patience to get your paperwork done?
- Do you wish you had more time to do the things you enjoy doing?
- Contact Barwick & Lund today and we will transform your chaos into order.

Underneath the slide show will be a button to "Call Barwick & Lund Now - 03 5550 1827".

```html
<!DOCTYPE html>
<html lang="en">
<head>
<meta charset="utf-8">
<title>Barwick &amp; Lund – Bookkeeping &amp; BAS Services</title>
<link rel="stylesheet" href="https://fonts.googleapis.com/css2?family=Ubuntu:wght@400;500;700&family=Arimo:wght@400;700&display=swap">
<style>
:root{
  --page:#f3f3f3;
  --white:#ffffff;
  --ink:#222222;
  --body:#3a3a3a;
  --brand:#8b0000;
  --brand-bright:#a30d0d;
  --nav-top:#333333;
  --nav-bottom:#050505;
  --tick:#4d8a1c;
  --rule:#d6d6d6;
}
*{box-sizing:border-box;margin:0;padding:0}
html,body{width:1200px;height:1200px;overflow:hidden}
body{background:var(--page);font-family:"Arimo",Arial,sans-serif;color:var(--ink);position:relative}
.site-header{position:absolute;left:0;top:0;width:1200px;height:78px;background:var(--white);border-bottom:1px solid var(--rule)}
.brand{position:absolute;left:120px;top:11px;width:300px;height:57px;border:1px solid #333;display:flex;align-items:center;gap:10px;padding-left:12px;background:var(--white)}
.brand-mark{width:22px;height:22px;background:var(--brand)}
.brand-name{font-family:"Ubuntu",sans-serif;font-weight:500;font-size:30px;color:var(--brand)}
.search{position:absolute;left:878px;top:27px;width:203px;height:25px;border:1px solid #c8c8c8;background:#f8f8f8;font-size:13px;color:#999;padding:5px 12px}
.main-nav{position:absolute;left:0;top:80px;width:1200px;height:56px;background:linear-gradient(var(--nav-top),var(--nav-bottom))}
.main-nav ul{list-style:none;display:flex;gap:20px;position:absolute;left:119px;top:20px}
.main-nav a{font-family:"Ubuntu",sans-serif;font-size:13px;color:#eee;text-decoration:none}
.main-nav a.current{font-weight:700;color:#fff}
.page{position:absolute;left:120px;top:136px;width:960px;height:1064px;background:var(--white)}
.hero{position:absolute;left:0;top:1px;width:960px;height:260px;background:var(--white);overflow:hidden}
.hero-photo{position:absolute;left:560px;top:0;width:400px;height:260px;background:linear-gradient(90deg,rgba(255,255,255,0) 0%,#d8d8d8 25%,#7a7a7a 60%,#2a2a2a 100%)}
.hero h1{position:absolute;z-index:2;left:40px;top:74px;font-family:"Arimo",Arial,sans-serif;font-size:36px;line-height:43px;font-weight:700;color:#111;white-space:nowrap}
.hero h1 em{font-style:normal;color:var(--brand)}
.slide-tabs{position:absolute;left:0;top:261px;width:960px;height:10px;display:flex;gap:2px;background:var(--white)}
.slide-tabs span{flex:1;background:#000}
.slide-tabs span.active{background:var(--brand-bright)}
.intro{position:absolute;left:0;top:271px;width:960px;height:120px;background:#f0f0f0}
.intro p{position:absolute;left:18px;top:25px;width:720px;font-family:"Ubuntu",sans-serif;font-weight:500;font-size:14.5px;line-height:19px;color:var(--brand)}
.call-btn{position:absolute;left:766px;top:26px;width:175px;height:33px;border-radius:3px;background:linear-gradient(#2d2d2d,#000);display:flex;align-items:center;overflow:hidden;text-decoration:none}
.call-btn .icon{width:32px;height:33px;background:var(--brand-bright);display:flex;align-items:center;justify-content:center}
.call-btn .label{flex:1;text-align:center;font-family:"Ubuntu",sans-serif;font-weight:700;font-size:16px;color:#fff;letter-spacing:.6px}
.phone{position:absolute;left:768px;top:68px;font-family:"Ubuntu",sans-serif;font-weight:700;font-size:25px;color:#222;letter-spacing:.5px}
h2{font-family:"Ubuntu",sans-serif;font-weight:500;font-size:18px;color:var(--brand);white-space:nowrap}
.col-left{position:absolute;left:15px;top:412px;width:530px}
.col-right{position:absolute;left:579px;top:418px;width:370px}
.welcome p{margin-top:14px;font-family:"Ubuntu",sans-serif;font-size:12.6px;line-height:17px;color:var(--body)}
.ticks{list-style:none;font-size:14.3px;color:#333}
.ticks li{position:relative;padding-left:20px;line-height:22px}
.ticks li svg{position:absolute;left:2px;top:5px}
.ticks a{color:var(--brand);text-decoration:underline}
.summary{position:absolute;left:0;top:240px;width:530px}
.summary .ticks{display:grid;grid-template-columns:270px 260px;margin-top:12px}
.different{position:absolute;left:1px;top:440px;width:530px}
.different .ticks{margin-top:13px}
.serve p{margin-top:14px;font-family:"Ubuntu",sans-serif;font-weight:500;font-size:12.6px;line-height:17px;color:#222}
.map{position:absolute;left:15px;top:118px;width:335px;height:305px;background:radial-gradient(ellipse at 55% 45%,#7c7c7c 0%,#a4a4a4 45%,#ffffff 72%)}
.quals{position:absolute;left:0;top:470px}
.quals h2{font-size:17px}
.quals .ticks{margin-top:15px}
</style>
</head>
<body>
<svg width="0" height="0" style="position:absolute">
  <symbol id="tick" viewBox="0 0 14 12"><path d="M1 6.5 L5 10.5 L13 1.5" fill="none" stroke="#4d8a1c" stroke-width="2.6" stroke-linecap="round"/></symbol>
</svg>

<header class="site-header">
  <div class="brand"><span class="brand-mark"></span><span class="brand-name">Barwick &amp; Lund</span></div>
  <div class="search">Search</div>
</header>

<nav class="main-nav">
  <ul>
    <li><a class="current" href="#">HOME</a></li>
    <li><a href="#">ABOUT US</a></li>
    <li><a href="#">SERVICES</a></li>
    <li><a href="#">TESTIMONIALS</a></li>
    <li><a href="#">ARTICLES</a></li>
    <li><a href="#">ENDORSEMENTS</a></li>
    <li><a href="#">LINKS</a></li>
    <li><a href="#">CONTACT US</a></li>
  </ul>
</nav>

<main class="page">
  <section class="hero">
    <div class="hero-photo" role="img" aria-label="Photo of two smiling business professionals in suits with a colleague working in the background"></div>
    <h1>Do you need to get <em>organised</em><br>for the end of financial year?</h1>
  </section>
  <div class="slide-tabs"><span></span><span class="active"></span><span></span><span></span><span></span><span></span><span></span></div>

  <section class="intro">
    <p>For nearly 10 years Barwick &amp; Lund has been servicing the local and interstate communities of Australia, providing first-class BAS and Bookkeeping services with a personal touch unmatched by anyone else in the country.</p>
    <a class="call-btn" href="#">
      <span class="icon"><svg width="20" height="18" viewBox="0 0 20 18"><path d="M2 6 Q10 0 18 6 L16 8 L13 6 L13 4 Q10 3 7 4 L7 6 L4 8 Z" fill="#fff"/><rect x="4" y="9" width="12" height="7" rx="1.5" fill="#fff"/><circle cx="10" cy="12.5" r="2" fill="#a30d0d"/></svg></span>
      <span class="label">CALL US NOW</span>
    </a>
    <div class="phone">03 5550 1827</div>
  </section>

  <div class="col-left">
    <section class="welcome">
      <h2>Welcome to Barwick &amp; Lund</h2>
      <p>Having worked a certified accountants firm for nomerous years. Helen Barwick &amp; Joanne Lund became concerned about consistency of innacurate book prepare by others in various organisation. As the quality of bookwork decline the fees seemed to increase. Together they identified a need for a quality bookkeeping service that truly understood that what being in business is all about and more importantly, how to correctly &amp; accurately process books according to the laws and requirements set by the Australian Taxation Office. They wanted to give people a better alternative - thus Barwick &amp; Lund was born. What began a small business focusing on family, friend and the local community, has since grown into a well respected business with 95% of their business base solely on word of mouth and personal referrals around Australia.</p>
    </section>

    <section class="summary">
      <h2>To summarise</h2>
      <ul class="ticks">
        <li><svg width="14" height="12"><use href="#tick"/></svg>FREE initial consultation</li>
        <li><svg width="14" height="12"><use href="#tick"/></svg>Superannuation &amp; Workcover</li>
        <li><svg width="14" height="12"><use href="#tick"/></svg><a href="#">Registered BAS Agent #41822-317</a></li>
        <li><svg width="14" height="12"><use href="#tick"/></svg>Margin Scheme</li>
        <li><svg width="14" height="12"><use href="#tick"/></svg>Bookkeeping</li>
        <li><svg width="14" height="12"><use href="#tick"/></svg>Fuel Tax Credits</li>
        <li><svg width="14" height="12"><use href="#tick"/></svg>BAS Preparation &amp; Lodgement</li>
        <li><svg width="14" height="12"><use href="#tick"/></svg>Offsite &amp; onsite bookkeeping</li>
        <li><svg width="14" height="12"><use href="#tick"/></svg>Payroll</li>
        <li><svg width="14" height="12"><use href="#tick"/></svg>LedgerPro Software &amp; Trainning</li>
        <li><svg width="14" height="12"><use href="#tick"/></svg>IAS Preparation &amp; Lodgement</li>
        <li><svg width="14" height="12"><use href="#tick"/></svg>Australia Wide</li>
      </ul>
    </section>

    <section class="different">
      <h2>What makes Barwick &amp; Lund different from other Bookeepers</h2>
      <ul class="ticks">
        <li><svg width="14" height="12"><use href="#tick"/></svg>We guarantee the quality of our work</li>
        <li><svg width="14" height="12"><use href="#tick"/></svg>We have over 35 years of experience</li>
        <li><svg width="14" height="12"><use href="#tick"/></svg>We have owned &amp; operated business for 35 years</li>
        <li><svg width="14" height="12"><use href="#tick"/></svg>The Barwick &amp; Lund team are investors &amp; traders</li>
        <li><svg width="14" height="12"><use href="#tick"/></svg>Extensive business network for your benefit</li>
        <li><svg width="14" height="12"><use href="#tick"/></svg>Backed by a team of Accountants</li>
        <li><svg width="14" height="12"><use href="#tick"/></svg>We work with a team of elite accountants &amp; wealth creation professionals who coach us monthly in the following:</li>
      </ul>
    </section>
  </div>

  <div class="col-right">
    <section class="serve">
      <h2>Servicing all of Australia</h2>
      <p>95% of our clients come from client &amp;accountan referrals. We have clients all over Victoria, Queensland, NSW &amp; Western Australia, so no matter where you are, we can help.</p>
      <div class="map" role="img" aria-label="Map of Australia by state, marking Perth, Adelaide and Hobart with population figures"></div>
    </section>

    <section class="quals">
      <h2>Qualifications, Memberships and Partnerships</h2>
      <ul class="ticks">
        <li><svg width="14" height="12"><use href="#tick"/></svg>Registered ATO BAS Agent</li>
        <li><svg width="14" height="12"><use href="#tick"/></svg>Certificate IV Financial Services</li>
        <li><svg width="14" height="12"><use href="#tick"/></svg>Certificate III Financial Services</li>
        <li><svg width="14" height="12"><use href="#tick"/></svg>Member of Guild of Certified Bookkeepers</li>
        <li><svg width="14" height="12"><use href="#tick"/></svg>Platinum members of National Bookkeepers Circle</li>
        <li><svg width="14" height="12"><use href="#tick"/></svg>LedgerPro Professional Partner</li>
        <li><svg width="14" height="12"><use href="#tick"/></svg>TaxWise Network</li>
      </ul>
    </section>
  </div>
</main>
</body>
</html>
```